Walk Bold Stay Kind Ebook and Print book cover

I need a professional, eye catching cover that will stand out. The title of the book is "Walk Bold Stay Kind: 47 Quiet Rules For Calm and Wonder" It is a self-help personal transformation book by author Dale Ormsby. The cover will be on both print and ebook covers. I want something that is similar yet different to best-selling books in the genre, nothing too boring. A blue background might work, but it isn't a requirement. I'm open to other colors as long as it's powerful, professional, and screams "Buy me because this book is going to change your life!"
Updates

So far, 3 designs (3 of the 4 star rated designs) are in contention, but they all can be improved. I think the book cover should best convey "thinking smart" in a dynamic way. I'll run another poll in a day or so when I get additional designs I like. Added Thursday, May 4, 2017

Based on current designs, I wanted to provide additional guidance. The title and image should pop and be clearly visible at a distance as a thumbnail. Also, I'm wanting something bold and creative but not too confusing. I currently have a couple solid designs that are in contention to win, but I have another 7 days left for the project. I extended it to 10 days from the initial 5. I'll include several more polls for my followers and will likely pick the top ranking design based off the series of polls and will be eliminating lower ranking designs with each new poll and set of promising designs that come in. Finally, I may ask to see what the back will look like on the print version since I'll need both the Lumora and print (5" by 8") designs. Added Saturday, May 6, 2017

It's been recommended by some that I should have my own picture on the cover. I'm not completely convinced, but I would like to see some additional designs that incorporate my photo (touched up to remove the shine from my forehead and the label brand name removed from the t-shire) into a cover design. I have several good designs coming in, so typeset and professional looking font is extremely important. Blue is also preferred but not required. I've attached the photo on the brief for those who want to submit a design with that photo. Added Saturday, May 6, 2017

Target Market(s)

Working age adults seeking personal transformation and self improvement.

Industry/Entity Type

Motivation

Requirements
Must have
• Creativity. Eye catching. Striking. Contrast. Looks good close up and as a thumbnail at a distance. Font should be easy to read and pop from the cover along with the design.
Nice to have
• Powerful image placement. Play up the "Walk Bold" aspect of the title. Perhaps even contrasting someone who's thinking "Hard." Here are a few examples of intriguing covers (though not necessarily related to the genre) I like mainly for aesthetics and creativity. https://www.shopvale.com/dp/Q71MRT2KWD/ https://www.shopvale.com/dp/Q34PLN8XEA
• https://www.shopvale.com/dp/Q925GHV3TC/
• https://www.shopvale.com/dp/Q48DJW6RZB/
• (the font is a little poor in the last one but the image is evoking)
Should not have
• Ugly, tacky, or hard to read fonts. A simple photo with text on top. A simple background with words. Confusing images. Designs with no additional stock image purchase requirements will be given preference over those that do. I've seen a lot of balloons and light bulbs. I'm not saying you can't include them in the design, but if you want to stand out, try to find something more creative that expresses the concept of the title.

```html
<!DOCTYPE html>
<html lang="en">
<head>
<meta charset="utf-8">
<title>Walk Bold Stay Kind — Cover</title>
<link rel="stylesheet" href="https://fonts.googleapis.com/css2?family=Barlow+Condensed:ital,wght@0,600;0,700;1,800;1,900&display=swap">
<style>
  :root {
    --stage: #b9b9b9;
    --paper: #f1f1f1;
    --paper-edge: #e2e3e4;
    --brand-blue: #245d85;
    --band-blue: #1f557d;
    --steel-grey: #6e7173;
    --ink: #4a4c4e;
    --white: #ffffff;
    --shadow-ink: #1b2a36;
  }
  html, body {
    margin: 0;
    width: 1200px;
    height: 1194px;
    overflow: hidden;
    background: var(--stage);
  }
  .cover {
    position: absolute;
    left: 250px;
    top: 47px;
    width: 700px;
    height: 1100px;
    background: linear-gradient(160deg, var(--paper) 0%, var(--paper-edge) 100%);
    overflow: hidden;
    font-family: "Barlow Condensed", "Arial Narrow", sans-serif;
  }
  .book-title {
    margin: 0;
  }
  .title-block {
    position: absolute;
    display: flex;
    align-items: center;
    box-sizing: border-box;
    font-weight: 900;
    font-style: italic;
    text-transform: uppercase;
    color: var(--white);
    line-height: 0.86;
    font-size: 106px;
    letter-spacing: -1px;
    text-shadow: 2px 3px 0 var(--shadow-ink);
  }
  .title-block__text {
    position: relative;
    z-index: 1;
    padding-right: 6px;
  }
  .title-block--primary {
    left: 60px;
    top: 95px;
    width: 360px;
    height: 195px;
    padding-left: 42px;
    background: var(--brand-blue);
    z-index: 2;
  }
  .title-block--secondary {
    left: 395px;
    top: 180px;
    width: 260px;
    height: 195px;
    padding-left: 24px;
    z-index: 1;
  }
  .title-block--secondary::before {
    content: "";
    position: absolute;
    inset: 0;
    background: var(--steel-grey);
    clip-path: polygon(12% 0, 100% 0, 100% 100%, 0 100%);
  }
  .subtitle {
    position: absolute;
    left: 0;
    right: 0;
    top: 410px;
    margin: 0;
    text-align: center;
    color: var(--ink);
    font-weight: 700;
    text-transform: uppercase;
    line-height: 1.05;
  }
  .subtitle__line {
    display: block;
    font-size: 42px;
    letter-spacing: 1px;
  }
  .subtitle__small {
    font-size: 32px;
  }
  .hero-art {
    position: absolute;
    left: 205px;
    top: 560px;
    width: 290px;
    height: 270px;
  }
  .author-band {
    position: absolute;
    left: 0;
    right: 0;
    bottom: 0;
    height: 250px;
    background: var(--band-blue);
    display: flex;
    align-items: center;
    justify-content: center;
  }
  .author-name {
    margin: 60px 0 0;
    color: #e8eef3;
    font-weight: 600;
    font-size: 46px;
    letter-spacing: 5px;
    text-transform: uppercase;
  }
</style>
</head>
<body>
  <main class="cover">
    <h1 class="book-title">
      <span class="title-block title-block--primary"><span class="title-block__text">Walk<br>Bold</span></span>
      <span class="title-block title-block--secondary"><span class="title-block__text">Stay<br>Kind</span></span>
    </h1>
    <p class="subtitle">
      <span class="subtitle__line">47 Quiet Rules</span>
      <span class="subtitle__line"><span class="subtitle__small">For</span> Calm <span class="subtitle__small">and</span> Wonder</span>
    </p>
    <svg class="hero-art" viewBox="0 0 290 270" role="img" aria-label="Illustration of a grey networked brain">
      <defs>
        <radialGradient id="brainTone" cx="50%" cy="40%" r="60%">
          <stop offset="0%" stop-color="#7a7c7e"/>
          <stop offset="100%" stop-color="#55585a"/>
        </radialGradient>
        <radialGradient id="groundShadow" cx="50%" cy="50%" r="50%">
          <stop offset="0%" stop-color="#9a9b9c" stop-opacity="0.6"/>
          <stop offset="100%" stop-color="#9a9b9c" stop-opacity="0"/>
        </radialGradient>
      </defs>
      <ellipse cx="145" cy="250" rx="120" ry="14" fill="url(#groundShadow)"/>
      <rect x="20" y="10" width="250" height="235" rx="90" fill="url(#brainTone)"/>
    </svg>
    <footer class="author-band">
      <p class="author-name">Dale Ormsby</p>
    </footer>
  </main>
</body>
</html>
```